Gift card design to reflect the theme from our overhead business sign

We need a gift card that aligns with our colors used for the sign. Since I am not sure what you're able to do with the limited space, if you think you can create a miniature version of the sign and add the words "Gift Card" to it. I'd like to see it. I have also uploaded the original logo we use as an other variable to use in place the horizontal one on the sign. That might be alright too. Give me a few options to consider.

Then for the back of the card there may be some legal requirements for the wording. I'll get back to you on that. First, let's focus on the design.

Also, i am sending the requirements for "Tormix" who will be the processor for the card. I will be doing custom cards so pay attention to page 4.

After the gift card, I will sending you the front of the store image with the sign in place, so you can come up with some ideas for a simple window design to go across all the windows.

How fast can you get back to me? Unlike the sign, I'm sort of in a time crunch.

Oh, one other thing, I want to change the pink in our current logo to the pink you used in the sign. So if you use our standard logo, please change the pink to the on you used for the sign.

```html
<!DOCTYPE html>
<html lang="en">
<head>
<meta charset="utf-8">
<title>Gift Card – The Bake Parlor</title>
<link rel="stylesheet" href="https://fonts.googleapis.com/css2?family=Comfortaa:wght@700&display=swap">
<style>
  :root {
    --page-bg: #e4e4e4;
    --frame-green: #b2d449;
    --frame-orange: #f7932e;
    --card-pink: #ee3c96;
    --shadow-pink: #b5266f;
    --text-white: #ffffff;
  }
  * { margin: 0; padding: 0; box-sizing: border-box; }
  html, body {
    width: 1200px;
    height: 960px;
    overflow: hidden;
    background: var(--page-bg);
  }
  .canvas {
    position: relative;
    width: 1200px;
    height: 960px;
  }
  .gift-card {
    position: absolute;
    left: 222px;
    top: 245px;
    width: 757px;
    height: 472px;
    background: var(--frame-green);
    border-radius: 20px;
    padding: 27px;
  }
  .card-face {
    position: relative;
    width: 100%;
    height: 100%;
    background: var(--card-pink);
    padding: 11px;
  }
  .orange-frame {
    width: 100%;
    height: 100%;
    border: 12px solid var(--frame-orange);
    display: flex;
    flex-direction: column;
    align-items: center;
  }
  .card-title {
    margin-top: 48px;
    font-family: "Comfortaa", sans-serif;
    font-weight: 700;
    font-size: 96px;
    line-height: 1;
    letter-spacing: -1px;
    color: var(--text-white);
    text-shadow: 6px 6px 0 var(--shadow-pink), 11px 11px 0 var(--shadow-pink);
  }
  .brand-name {
    margin-top: 96px;
    font-family: "Comfortaa", sans-serif;
    font-weight: 700;
    font-size: 68px;
    line-height: 1;
    letter-spacing: -1px;
    color: var(--text-white);
    white-space: nowrap;
  }
</style>
</head>
<body>
  <main class="canvas">
    <section class="gift-card" aria-label="Gift card front">
      <div class="card-face">
        <div class="orange-frame">
          <h1 class="card-title">Gift Card</h1>
          <p class="brand-name">The Bake Parlor</p>
        </div>
      </div>
    </section>
  </main>
</body>
</html>
```